Letterhead design for Sleep Consulting Business

I'm looking for a new letterhead (heading/footer) design for my Sleep Consulting Business, I work with families to help their children improve their sleep.

The heading/footer will used in Microsoft Word Only-to be used for all of my documents such as writing Sleep Plans. I need to utilize as much working space in the document as possible. This will NOT be printed out on paper- it will only be used for heading/footer on microsoft word, then emailed to clients, who may print it at home.

My brand colors:
Dark Blue Hex: 1F2A42
Lighter Blueish Hex: 90BEC9
You're welcome to check out my website for inspiration- it is freshly created with other colors as well, and I love the outcome. www.quietharborsleep.example

Target Market(s)

Tired parents

Font styles to use
Script
Other font styles liked:
• Great Vibe, Lato or Just Another Hand are all used currently for my brand. Open to other options.

Requirements
Must have
• The letterhead (heading/footer) MUST be kept narrow (height-wise), so I have plenty of space on my document, while including important information.

It should look professional on screen, and when printed.

Must include my business name OR logo (Quiet Harbor Sleep Consulting), and my email address. Tessa@quietharborsleep.example

Website is optional, not required, just if you need to fill in a spot: www.quietharborsleep.example

```html
<!DOCTYPE html>
<html lang="en">
<head>
<meta charset="utf-8">
<title>Quiet Harbor Sleep Consulting Letterhead</title>
<link href="https://fonts.googleapis.com/css2?family=Great+Vibes&family=Lato:wght@400;700&display=swap" rel="stylesheet">
<style>
  :root {
    --navy: #1f2a42;
    --sky: #90bec9;
    --paper: #eeeded;
    --backdrop: #9fb5b6;
    --ink: #2e2e30;
    --muted: #7a7a7a;
    --accent: #b01e22;
  }
  * { box-sizing: border-box; margin: 0; padding: 0; }
  html, body { width: 1192px; height: 1200px; overflow: hidden; }
  body { background: var(--backdrop); font-family: 'Lato', sans-serif; position: relative; }

  .letterhead {
    position: absolute; left: 199px; top: 40px;
    width: 794px; height: 1120px;
    background: var(--paper);
    border-top: 3px solid var(--navy);
    border-bottom: 3px solid var(--navy);
    box-shadow: 0 6px 24px rgba(0,0,0,.18);
  }

  .edge-bar { position: absolute; left: 0; width: 6px; background: var(--navy); }
  .edge-bar--top { top: 166px; height: 70px; }
  .edge-bar--middle { top: 338px; height: 428px; }
  .edge-bar--bottom { top: 914px; height: 72px; }

  .brand { position: absolute; left: 24px; top: 28px; display: flex; align-items: center; gap: 16px; }
  .brand-dot { width: 78px; height: 78px; border-radius: 50%; background: var(--navy); }
  .brand-name { font-weight: 400; font-size: 34px; color: var(--navy); line-height: 1; }
  .brand-name small { display: block; font-size: 12px; letter-spacing: 3px; margin-top: 10px; text-align: center; }

  .contact { position: absolute; right: 16px; top: 24px; width: 184px; }
  .contact-name { font-family: 'Great Vibes', cursive; font-size: 17px; color: var(--navy); white-space: nowrap; text-align: right; }
  .contact-list { list-style: none; margin-top: 4px; border-left: 2px solid #2f6f9e; padding-left: 8px; }
  .contact-list li { font-size: 10.5px; color: #111; line-height: 16px; display: flex; align-items: center; gap: 4px; white-space: nowrap; }
  .contact-list svg { width: 9px; height: 9px; flex: none; }

  .letter { position: absolute; left: 60px; top: 198px; width: 610px; color: var(--ink); }
  .letter-to { font-size: 15px; font-weight: 700; margin-bottom: 20px; }
  .recipient-name { font-size: 17px; color: var(--accent); line-height: 18px; letter-spacing: .5px; }
  .recipient-role { font-size: 11px; color: var(--muted); line-height: 12px; }
  .recipient-line { font-size: 17px; line-height: 18.5px; }
  .letter-body { margin-top: 18px; font-size: 16px; line-height: 18.5px; }
  .letter-body p { margin-bottom: 18px; }
  .letter-body p.wide-gap { margin-bottom: 36px; }
</style>
</head>
<body>
  <main class="letterhead">
    <span class="edge-bar edge-bar--top"></span>
    <span class="edge-bar edge-bar--middle"></span>
    <span class="edge-bar edge-bar--bottom"></span>

    <header>
      <div class="brand">
        <span class="brand-dot"></span>
        <div class="brand-name">Quiet Harbor<small>SLEEP CONSULTING</small></div>
      </div>

      <div class="contact">
        <div class="contact-name">Quiet Harbor Sleep Consulting</div>
        <ul class="contact-list">
          <li><svg viewBox="0 0 10 10"><path d="M2 1l2 2-1 1.2a6 6 0 0 0 2.8 2.8L7 6l2 2-1.2 1.2C4.5 9 1 5.5.8 2.2z" fill="#1f2a42"/></svg>555-014-2290</li>
          <li><svg viewBox="0 0 10 10"><rect x=".7" y="2" width="8.6" height="6" fill="none" stroke="#1f2a42" stroke-width=".9"/><path d="M.7 2L5 5.5 9.3 2" fill="none" stroke="#1f2a42" stroke-width=".9"/></svg>tessa@quietharborsleep.example</li>
          <li><svg viewBox="0 0 10 10"><circle cx="5" cy="5" r="4.2" fill="none" stroke="#1f2a42"/><path d="M.8 5h8.4M5 .8c-2.2 2.5-2.2 5.9 0 8.4M5 .8c2.2 2.5 2.2 5.9 0 8.4" fill="none" stroke="#1f2a42" stroke-width=".8"/></svg>www.quietharborsleep.example</li>
        </ul>
      </div>
    </header>

    <section class="letter">
      <p class="letter-to">TO</p>
      <p class="recipient-name">HARPER</p>
      <p class="recipient-role">Director</p>
      <p class="recipient-line">Design Studio</p>
      <p class="recipient-line">A: 555 010 254</p>
      <p class="recipient-line">B:555 0145 475</p>

      <div class="letter-body">
        <p>Lorem ipsum dolor sit amet, consectetur adipiscing elit. Vestibulum consectetur egestas metus, quis scelerisque tortor consectetur sed. Nullam sit amet lorem sed arcu faucibus semper. Vestibulum ante ipsum primis in faucibus orci luctus et ultrices posuere cubilia Curae; Sed sagittis arcu ut ligula molestie malesuada. Suspendisse posuere tincidunt elit, at ullamcorper augue blandit vitae.</p>
        <p>Cras egestas vestibulum pulvinar. Donec iaculis imperdiet hendrerit. Sed mollis, enim quis hendrerit dictum, tortor mauris vulputate ligula, viverra porta magna libero at mi. Integer odio nisl, luctus nec dui in, rutrum sollicitudin nisi. Suspendisse nec erat eros.</p>
        <p class="wide-gap">Sed dictum quam arcu, sit amet ullamcorper orci faucibus eget. Morbi finibus ante at risus commodo, nec ullamcorper nulla tincidunt. Integer eu molestie nulla, sed consequat tortor. Sed ullamcorper congue metus, vitae dictum nibh luctus sed. Suspendisse ornare purus fermentum, viverra elit sed, bibendum ex. Vivamus semper diam vel diam laoreet rutrum. Ut porta fermentum velit. Vestibulum vitae semper nisl. Sed facilisis at ex et vestibulum. Donec at magna ut eros pulvinar hendrerit.</p>
        <p>Sed dictum quam arcu, sit amet ullamcorper orci faucibus eget. Morbi finibus ante at risus commodo, nec ullamcorper nulla tincidunt. Integer eu molestie nulla, sed consequat tortor. Sed ullamcorper congue metus, vitae dictum nibh luctus sed. Suspendisse ornare purus fermentum, viverra elit sed, bibendum ex.</p>
        <p>Vivamus semper diam vel diam laoreet rutrum. Ut porta fermentum velit. Vestibulum vitae semper nisl. Sed facilisis at ex et vestibulum. Donec at magna ut eros pulvinar hendrerit.</p>
      </div>
    </section>
  </main>
</body>
</html>
```